Independent IT Consulting Professional. Looking for a clean crisp, somewhat traditional design. I have also attached the initial off-the-shelf design from PrintNook. My company has grown quickly, and I would like to take the card to the next level. Should be sharp, mature, classy well laid-out and convey confidence. I don't think the off-the-shelf design does this. I like the logo I have for the time being, but if someone has something better in mind, I would be happy to consider an alternative. I would also like to see the color Cyan used in a small way, either with the logo or some other color treatment, as I feel like this is a modern color that I always liked, but never was able to make anything work with it.
Industry/Entity Type
It Company
Contact Information for Business Card
Garrett L. Ostrander
Owner
TechHollow Solutions
2817 Marwood Lane
Brevard, NY 13592
(917) 555-0147
gostrander@techhollowsolutions.example
www.techhollowsolutions.example
Tagline: Business Technology Services and Consulting

```html
<!DOCTYPE html>
<html lang="en">
<head>
<meta charset="utf-8">
<title>TechHollow Solutions – Business Card</title>
<link rel="stylesheet" href="https://fonts.googleapis.com/css2?family=Source+Sans+3:wght@400;600;700&display=swap">
<style>
  :root {
    --backdrop: #ece9e4;
    --card-white: #ffffff;
    --card-cyan: #82fbe0;
    --ink: #222222;
    --brand-blue: #2f6fe0;
    --tag-blue: #1f5fd6;
    --band-black: #111111;
    --logo-ink: #1a1a1a;
  }
  * { box-sizing: border-box; margin: 0; padding: 0; }
  html, body { width: 1200px; height: 469px; overflow: hidden; }
  body {
    background: var(--backdrop);
    font-family: "Source Sans 3", "Myriad Pro", sans-serif;
    position: relative;
  }
  .card {
    position: absolute;
    top: 85px;
    width: 520px;
    height: 300px;
    overflow: hidden;
    box-shadow: 0 4px 14px rgba(0,0,0,0.25);
  }
  .card--front { left: 40px; background: var(--card-white); color: var(--ink); }
  .card--back  { left: 640px; background: var(--card-cyan); }

  .front-wordmark {
    position: absolute;
    top: 44px; left: 0; right: 0;
    text-align: center;
    font-weight: 700;
    font-size: 38px;
    line-height: 1;
    color: var(--logo-ink);
  }
  .front-wordmark .mark-dot {
    display: inline-block;
    width: 14px; height: 14px;
    background: var(--brand-blue);
    border-radius: 50%;
    margin-right: 10px;
    vertical-align: middle;
  }

  .holder { position: absolute; left: 34px; top: 158px; }
  .holder__name { font-weight: 700; font-size: 19px; line-height: 22px; color: var(--brand-blue); }
  .holder__role { font-size: 15px; line-height: 18px; margin-top: 4px; }

  .contact { position: absolute; left: 34px; top: 204px; font-size: 13px; line-height: 18px; }
  .contact__row { display: flex; align-items: center; gap: 5px; }
  .contact svg { width: 11px; height: 11px; }

  .address {
    position: absolute; right: 30px; top: 140px;
    text-align: right; font-size: 13.5px; line-height: 20px;
  }
  .web {
    position: absolute; right: 30px; top: 198px;
    display: flex; align-items: center; gap: 5px; font-size: 13px; line-height: 18px;
  }
  .web svg { width: 11px; height: 11px; }

  .bands { position: absolute; left: 0; top: 244px; width: 520px; height: 20px; overflow: visible; }
  .tagline-front {
    position: absolute; left: 0; right: 0; bottom: 8px;
    text-align: center; font-size: 17px; line-height: 20px; color: var(--ink);
  }

  .back-wordmark {
    position: absolute; top: 108px; left: 0; right: 0;
    text-align: center;
    font-weight: 700; font-size: 46px; line-height: 1;
    color: var(--card-white);
  }
  .tagline-back {
    position: absolute; top: 186px; left: 0; right: 0;
    text-align: center; font-size: 19px; color: var(--tag-blue);
  }
</style>
</head>
<body>

<section class="card card--front" aria-label="Business card front">
  <div class="front-wordmark"><span class="mark-dot"></span>TechHollow Solutions</div>

  <div class="address">
    <div>2817 Marwood Lane</div>
    <div>Brevard, NY 13592</div>
  </div>

  <div class="holder">
    <div class="holder__name">Garrett L. Ostrander</div>
    <div class="holder__role">Owner</div>
  </div>

  <div class="contact">
    <div class="contact__row">
      <svg viewBox="0 0 12 12" aria-hidden="true"><circle cx="6" cy="6" r="5.3" fill="none" stroke="#222" stroke-width="1"/><path d="M4 3.2l1.2 1.3-.6.8c.4.9 1 1.5 1.9 1.9l.8-.6 1.3 1.2-.8.9C5.9 8.5 3.6 6.2 3.3 4z" fill="#222"/></svg>
      <span>(917) 555-0147</span>
    </div>
    <div class="contact__row">
      <svg viewBox="0 0 12 12" aria-hidden="true"><circle cx="6" cy="6" r="5.8" fill="#222"/><rect x="3" y="4" width="6" height="4.2" fill="#fff"/><path d="M3 4l3 2.3L9 4" fill="none" stroke="#222" stroke-width=".8"/></svg>
      <span>gostrander@techhollowsolutions.example</span>
    </div>
  </div>

  <div class="web">
    <svg viewBox="0 0 12 12" aria-hidden="true"><circle cx="6" cy="6" r="5.3" fill="none" stroke="#222" stroke-width="1"/><ellipse cx="6" cy="6" rx="2.2" ry="5.3" fill="none" stroke="#222" stroke-width=".8"/><path d="M.8 6h10.4M1.8 3.5h8.4M1.8 8.5h8.4" stroke="#222" stroke-width=".7"/></svg>
    <span>www.techhollowsolutions.example</span>
  </div>

  <svg class="bands" viewBox="0 0 520 20" aria-hidden="true">
    <polygon points="0,10 290,0 290,8 0,18" fill="var(--band-black)"/>
    <polygon points="300,0 520,-10 520,-2 296,8" fill="var(--brand-blue)"/>
  </svg>

  <div class="tagline-front">Business Technology Services and Consulting</div>
</section>

<section class="card card--back" aria-label="Business card back">
  <div class="back-wordmark">TechHollow Solutions</div>
  <div class="tagline-back">Business Technology Services and Consulting</div>
</section>

</body>
</html>
```